Auto Mechanic business card

Need a general business card for GearFixer.
Name on card should be 'Roadside Wrench'
Tel # (869) 412 3097
Address is - Palm Lane, Basseterre, St. Kitts
Whatsapp and facebook symbols should be added
On back of card should include services offered
General Repairs
Brakes
Tune Ups
Suspensions
Oil Leaks
Dent repairs
Suspensions
Car Sales
Tyre Repairs
General service
Check Engine Light
Minor Electricals

Target Market(s)

General Population, University students

Industry/Entity Type

Auto Mechanic

Contact Information for Business Card

Roadside Wrench

Requirements
Must have
• 2 Sides

```html
<!DOCTYPE html>
<html lang="en">
<head>
<meta charset="utf-8">
<title>Roadside Wrench – Business Card</title>
<link rel="stylesheet" href="https://fonts.googleapis.com/css2?family=Chakra+Petch:wght@400;500;700&display=swap">
<style>
  :root {
    --backdrop: #e31e25;
    --card-black: #050404;
    --plate-tone: #140807;
    --brand-red: #e31e25;
    --white: #ffffff;
  }
  * { margin: 0; padding: 0; box-sizing: border-box; }
  html, body { width: 1200px; height: 900px; overflow: hidden; }
  body {
    background: var(--backdrop);
    font-family: "Chakra Petch", "Arial Narrow", sans-serif;
    position: relative;
  }
  .card {
    position: absolute;
    left: 284px;
    width: 632px;
    height: 361px;
    border-radius: 28px;
    overflow: hidden;
    background: var(--card-black);
  }
  .card--services { top: 80px; }
  .card--contact { top: 459px; }
  .plate-texture {
    position: absolute; inset: 0;
    background: radial-gradient(ellipse at 60% 40%, var(--plate-tone), var(--card-black) 75%);
  }
  .card-band {
    position: absolute; left: 0; right: 0; bottom: 0; height: 11px;
    background: var(--white);
  }
  .card-band__red {
    position: absolute; left: 0; top: 0; bottom: 0;
    background: var(--brand-red);
    clip-path: polygon(0 0, 100% 0, calc(100% - 3px) 100%, 0 100%);
  }
  .card--services .card-band__red { width: 404px; }
  .card--contact .card-band__red { width: 222px; }

  .service-group { position: absolute; top: 78px; }
  .service-group--repairs { left: 71px; }
  .service-group--general { left: 358px; }
  .service-group__title {
    color: var(--white);
    font-size: 17.5px; font-weight: 400; letter-spacing: 1px;
    line-height: 1; margin-bottom: 16px;
  }
  .service-list { list-style: none; }
  .service-list li {
    color: var(--brand-red);
    font-size: 18px; font-weight: 500; letter-spacing: 1px;
    line-height: 22.6px;
  }
  .service-list li::before { content: "»"; display: inline-block; width: 20px; }

  .brand-name {
    position: absolute;
    color: var(--white);
    font-weight: 700;
    text-transform: uppercase;
    white-space: nowrap;
    line-height: 1;
  }
  .card--services .brand-name { left: 310px; top: 278px; font-size: 25px; letter-spacing: 0.5px; }
  .card--contact .brand-name { left: 71px; top: 64px; font-size: 49px; letter-spacing: 1px; }

  .contact-phone {
    position: absolute; left: 71px; top: 142px;
    color: var(--white); font-size: 27px; font-weight: 400; letter-spacing: 1px;
  }
  .contact-address {
    position: absolute; left: 71px; top: 181px;
    color: var(--white); font-size: 17px; font-weight: 500; letter-spacing: 1px;
    line-height: 21px; font-style: normal;
  }
  .social-marks { position: absolute; left: 71px; top: 234px; display: flex; gap: 3px; }
  .social-mark { width: 28px; height: 28px; border-radius: 50%; background: var(--brand-red); }
</style>
</head>
<body>

<section class="card card--services" aria-label="Card back – services">
  <div class="plate-texture" role="img" aria-label="Dark diamond plate texture"></div>
  <div class="service-group service-group--repairs">
    <h2 class="service-group__title">GENERAL REPAIRS</h2>
    <ul class="service-list">
      <li>BRAKES TUNE UPS</li>
      <li>SUSPENSIONS</li>
      <li>OIL LEAKS</li>
      <li>DENT REPAIRS</li>
      <li>SUSPENSIONS</li>
      <li>CAR SALES</li>
      <li>TYRE REPAIRS</li>
    </ul>
  </div>
  <div class="service-group service-group--general">
    <h2 class="service-group__title">GENERAL SERVICE</h2>
    <ul class="service-list">
      <li>CHECK ENGINE LIGHT</li>
      <li>MINOR ELECTRICALS</li>
    </ul>
  </div>
  <p class="brand-name">Roadside Wrench</p>
  <div class="card-band"><div class="card-band__red"></div></div>
</section>

<section class="card card--contact" aria-label="Card front – contact">
  <div class="plate-texture" role="img" aria-label="Dark diamond plate texture"></div>
  <h1 class="brand-name">Roadside Wrench</h1>
  <p class="contact-phone">(869) 412 3097</p>
  <address class="contact-address">PALM LANE, BASSETERRE,<br>ST. KITTS</address>
  <div class="social-marks">
    <span class="social-mark" role="img" aria-label="Messaging app"></span>
    <span class="social-mark" role="img" aria-label="Social page"></span>
  </div>
  <div class="card-band"><div class="card-band__red"></div></div>
</section>

</body>
</html>
```